Harbor Petroleum Business Cards

I would like to design some options for about 10 sets of double sided business cards for our team with a raised logo with a Silver glossy finished logo. We are a privately funded upstream Oil & Gas producer drilling vertical wells in Central Oklahoma with a long term production (ROI driven) strategy that we implement through an annual drilling program. We are focused on a shallow / vertical / long life / low decline strategy. We are based in downtown Tulsa Oklahoma. I have attached a sample business card and a picture of our hallway logo which we would like to replicate on the business cards.

Target Market(s)

SEC Accredited Investors and other Oil & Gas Operators

Industry/Entity Type

Upstream Oil & Gas

Contact Information for Business Card

You can see the sample photo attached, but email / website / address / direct phone / Cell Phone / Name / Title / Fax

Font styles to use
Other font styles liked:
• Felix Titling

Colors
0054AA
0677BA
7BADD7
CADEEF
E8F1F8

Requirements
Must have
• Glossy raised logo
Nice to have
• Possibly a new logo.
Should not have
• No Greens /

```html
<!DOCTYPE html>
<html lang="en">
<head>
<meta charset="utf-8">
<title>Harbor Petroleum Business Cards</title>
<link rel="stylesheet" href="https://fonts.googleapis.com/css2?family=Cinzel:wght@400;600&family=Poppins:wght@400&display=swap">
<style>
  :root {
    --stage: #1f1f1f;
    --blue-deep: #0054AA;
    --blue-mid: #0677BA;
    --blue-soft: #7BADD7;
    --blue-pale: #CADEEF;
    --white: #ffffff;
  }
  * { margin: 0; padding: 0; box-sizing: border-box; }
  html, body { width: 1200px; height: 1200px; overflow: hidden; background: var(--stage); }
  .sheet {
    width: 1200px; height: 1200px;
    display: flex; flex-direction: column; align-items: center; justify-content: center; gap: 60px;
  }
  .card {
    position: relative;
    width: 840px; height: 480px;
    border-radius: 26px;
    background: linear-gradient(135deg, var(--blue-deep) 0%, var(--blue-mid) 100%);
    color: var(--white);
    font-family: "Poppins", sans-serif;
    overflow: hidden;
  }
  .company-name {
    font-family: "Poppins", sans-serif;
    font-weight: 400;
    color: var(--white);
    white-space: nowrap;
  }

  /* Front */
  .card-front .company-name {
    position: absolute; left: 0; right: 0; top: 200px;
    text-align: center; font-size: 48px; letter-spacing: 1px;
  }
  .card-front .site {
    position: absolute; left: 0; right: 0; bottom: 56px;
    text-align: center; font-size: 19px; letter-spacing: 0.5px;
  }

  /* Back */
  .card-back .company-name {
    position: absolute; left: 56px; top: 50px;
    font-size: 40px; letter-spacing: 0.5px;
  }
  .person { position: absolute; left: 56px; top: 150px; right: 56px; }
  .person-name { font-family: "Cinzel", serif; font-size: 32px; font-weight: 600; letter-spacing: 1px; }
  .person-title {
    font-family: "Cinzel", serif; font-size: 18px; color: var(--blue-pale);
    line-height: 1.35; margin-top: 6px; padding-bottom: 14px;
    border-bottom: 1px solid var(--blue-soft);
  }
  .contact-list { list-style: none; position: absolute; left: 56px; top: 310px; }
  .contact-list li { display: flex; align-items: center; gap: 16px; font-size: 19px; line-height: 30px; }
  .contact-list svg { width: 20px; height: 20px; fill: none; stroke: var(--blue-pale); stroke-width: 1.8; }
  .address {
    position: absolute; right: 56px; bottom: 48px;
    font-style: normal; text-align: right; font-size: 20px; line-height: 32px;
  }
</style>
</head>
<body>
<main class="sheet">
  <section class="card card-front">
    <div class="company-name">Harbor Petroleum LLC</div>
    <p class="site">www.HarborPetroleumLLC.com</p>
  </section>

  <section class="card card-back">
    <div class="company-name">Harbor Petroleum LLC</div>
    <div class="person">
      <h1 class="person-name">DORIAN K. WHITFIELD, CPL</h1>
      <p class="person-title">EXECUTIVE VICE PRESIDENT<br>LAND, LEGAL &amp; BUSINESS DEVELOPMENT</p>
    </div>
    <ul class="contact-list">
      <li><svg viewBox="0 0 24 24"><path d="M5 3h4l2 5-3 2a11 11 0 0 0 6 6l2-3 5 2v4a2 2 0 0 1-2 2A17 17 0 0 1 3 5a2 2 0 0 1 2-2z"/></svg>539-555-0142</li>
      <li><svg viewBox="0 0 24 24"><rect x="6" y="2" width="12" height="20" rx="2"/><path d="M11 18h2"/></svg>918-555-0187</li>
      <li><svg viewBox="0 0 24 24"><path d="M7 9V3h10v6"/><rect x="3" y="9" width="18" height="8" rx="1"/><path d="M7 14h10v7H7z"/></svg>918-555-0163</li>
      <li><svg viewBox="0 0 24 24"><rect x="3" y="5" width="18" height="14" rx="1"/><path d="M3 6l9 7 9-7"/></svg>DKW@HPTulsa.com</li>
      <li><svg viewBox="0 0 24 24"><circle cx="12" cy="12" r="9"/><path d="M3 12h18M12 3c3 3 3 15 0 18M12 3c-3 3-3 15 0 18"/></svg>www.HarborPetroleumLLC.com</li>
    </ul>
    <address class="address">220 South Main St<br>Suite 800<br>Tulsa, Ok 74103</address>
  </section>
</main>
</body>
</html>
```